Electrical Panel Hazard

We are looking for a mail out flyer explaining common household electrical panels are now deemed a fire hazard making homes containing these panels unable to be insured. We are looking to have clients check their home for a panel or breaker made by
Granite Meridian, Pathwarden, Vorlex, Brackmoor or Gript-hold. The final design should inform clients of the hazard and recommend an inspection and possible replacement.

Company name: Oakhurst Building Services Inc
Phone Number: (555)-204-3187

Industry/Entity Type

Electrical

```html
<!DOCTYPE html>
<html lang="en">
<head>
<meta charset="utf-8">
<title>Oakhurst Building Services Inc – Electrical Panel Hazard</title>
<link rel="stylesheet" href="https://fonts.googleapis.com/css2?family=Oswald:wght@500;600&family=Roboto+Condensed:wght@400;700&family=Open+Sans:wght@700&display=swap">
<style>
  :root {
    --navy: #0a2a68;
    --blue: #0b4ea2;
    --orange: #f6921e;
    --ink: #2e3192;
    --text: #333333;
    --paper: #f3f3f3;
    --white: #ffffff;
  }
  * { margin: 0; padding: 0; box-sizing: border-box; }
  html, body { width: 1006px; height: 1200px; overflow: hidden; background: var(--paper); }
  .flyer { position: relative; width: 1006px; height: 1200px; overflow: hidden; font-family: "Roboto Condensed", Arial, sans-serif; }
  .backdrop { position: absolute; inset: 0; }

  .brand { position: absolute; top: 40px; right: 36px; color: var(--white); font-family: "Roboto Condensed", Arial, sans-serif; font-weight: 700; font-size: 27px; line-height: 1.15; text-align: left; letter-spacing: 0.5px; display: flex; align-items: center; gap: 14px; }
  .brand-dot { width: 14px; height: 14px; border-radius: 50%; background: var(--orange); }

  .headline { position: absolute; top: 560px; left: 0; width: 100%; text-align: center; font-family: "Oswald", Impact, sans-serif; font-weight: 600; font-size: 64px; color: var(--ink); letter-spacing: 0.5px; line-height: 1; }
  .warning { position: absolute; top: 638px; left: 0; width: 100%; text-align: center; color: var(--text); font-size: 23px; line-height: 34px; }
  .warning strong { font-weight: 700; }

  .brands { position: absolute; top: 744px; left: 0; width: 100%; display: flex; justify-content: center; gap: 26px; list-style: none; color: var(--ink); font-weight: 700; font-size: 23px; }
  .brands li { display: flex; align-items: center; gap: 8px; }
  .brands svg { width: 19px; height: 19px; }

  .gallery { position: absolute; top: 818px; left: 0; width: 100%; height: 240px; }
  .gallery figure { position: absolute; top: 0; width: 220px; height: 220px; border-radius: 50%; border: 3px solid var(--orange); padding: 5px; background: var(--white); }
  .gallery figure::after { content: ""; position: absolute; left: 30px; right: 30px; bottom: -28px; height: 12px; border-radius: 50%; background: radial-gradient(ellipse, rgba(0,0,0,0.28), rgba(0,0,0,0) 70%); }
  .gallery .photo { width: 100%; height: 100%; border-radius: 50%; }
  .gallery .panel-one { left: 80px; }
  .gallery .panel-two { left: 396px; }
  .gallery .panel-three { left: 697px; }
  .panel-one .photo { background: radial-gradient(circle at 45% 45%, #6d6a66, #2c2a28 75%); }
  .panel-two .photo { background: linear-gradient(135deg, #cfd3d6 0%, #e8b93a 45%, #2b6cc4 80%); }
  .panel-three .photo { background: radial-gradient(circle at 50% 50%, #5a544e, #26221f 75%); }

  .footer-call { position: absolute; left: 0; top: 1083px; width: 502px; height: 117px; background: linear-gradient(90deg, var(--blue), var(--navy)); color: var(--orange); font-family: "Oswald", Impact, sans-serif; font-weight: 500; text-align: center; }
  .footer-call .cta { margin-top: 14px; font-size: 31px; line-height: 1; }
  .footer-call .phone { margin-top: 10px; font-size: 38px; line-height: 1; display: flex; justify-content: center; align-items: center; gap: 26px; }
  .footer-call .phone svg { width: 38px; height: 38px; }

  .footer-info { position: absolute; left: 503px; top: 1083px; width: 503px; height: 117px; background: var(--orange); color: var(--white); font-family: "Open Sans", Arial, sans-serif; font-weight: 700; text-align: center; }
  .footer-info .email { margin-top: 16px; font-size: 23px; }
  .footer-info .license { margin-top: 10px; font-size: 18px; line-height: 23px; }
</style>
</head>
<body>
<main class="flyer">
  <svg class="backdrop" viewBox="0 0 1006 1200" width="1006" height="1200" aria-hidden="true">
    <defs>
      <linearGradient id="houseFire" x1="0" y1="0" x2="1" y2="1">
        <stop offset="0" stop-color="#3c6b2c"/>
        <stop offset="0.35" stop-color="#8aa0bf"/>
        <stop offset="0.6" stop-color="#e8902a"/>
        <stop offset="1" stop-color="#3f6a2e"/>
      </linearGradient>
      <linearGradient id="headerBlue" x1="0" y1="0" x2="1" y2="0">
        <stop offset="0" stop-color="#0b4ea2"/>
        <stop offset="1" stop-color="#0a2a68"/>
      </linearGradient>
    </defs>
    <rect width="1006" height="1200" fill="#f3f3f3"/>
    <rect class="hero-photo" role="img" aria-label="Photo of a blue house on fire with flames in windows and door" x="0" y="90" width="1006" height="540" fill="url(#houseFire)"/>
    <path d="M0 0 H1006 V338 C800 178 420 114 0 128 Z" fill="#f6921e"/>
    <path d="M0 0 H1006 V322 C800 162 420 100 0 112 Z" fill="#ffffff"/>
    <path d="M0 0 H1006 V312 C800 152 420 92 0 104 Z" fill="url(#headerBlue)"/>
    <path d="M0 560 Q503 418 1006 548 V1200 H0 Z" fill="#0b4ea2"/>
    <path d="M0 568 Q503 430 1006 556 V1200 H0 Z" fill="#ffffff"/>
    <path d="M0 576 Q503 440 1006 562 V1200 H0 Z" fill="#f6921e"/>
    <path d="M0 600 Q503 462 1006 590 V1200 H0 Z" fill="#f3f3f3"/>
  </svg>

  <header class="brand">
    <span class="brand-dot"></span>
    <span class="brand-name">Oakhurst Building<br>Services Inc</span>
  </header>

  <h1 class="headline">YOUR HOME MAY BE UNSAFE</h1>
  <p class="warning">
    NEW INSURANCE CODE MAY HAVE DEEMED YOUR HOMES ELECTRICAL PANEL<br>
    <strong>FIRE HAZARD</strong>, <strong>UNINSURABLE</strong> and a <strong>DANGER</strong> to your families safety!<br>
    CALL US IF YOUR HOMES ELECTRICAL PANEL OR BREAKERS ARE MADE BY:
  </p>

  <ul class="brands">
    <li><svg viewBox="0 0 20 20"><rect x="2" y="3" width="14" height="14" rx="3" fill="none" stroke="currentColor" stroke-width="2"/><path d="M6 10 l3 3 l9 -10" fill="none" stroke="currentColor" stroke-width="2.2"/></svg>GRANITE MERIDIAN</li>
    <li><svg viewBox="0 0 20 20"><rect x="2" y="3" width="14" height="14" rx="3" fill="none" stroke="currentColor" stroke-width="2"/><path d="M6 10 l3 3 l9 -10" fill="none" stroke="currentColor" stroke-width="2.2"/></svg>PATHWARDEN</li>
    <li><svg viewBox="0 0 20 20"><rect x="2" y="3" width="14" height="14" rx="3" fill="none" stroke="currentColor" stroke-width="2"/><path d="M6 10 l3 3 l9 -10" fill="none" stroke="currentColor" stroke-width="2.2"/></svg>VORLEX</li>
    <li><svg viewBox="0 0 20 20"><rect x="2" y="3" width="14" height="14" rx="3" fill="none" stroke="currentColor" stroke-width="2"/><path d="M6 10 l3 3 l9 -10" fill="none" stroke="currentColor" stroke-width="2.2"/></svg>BRACKMOOR</li>
    <li><svg viewBox="0 0 20 20"><rect x="2" y="3" width="14" height="14" rx="3" fill="none" stroke="currentColor" stroke-width="2"/><path d="M6 10 l3 3 l9 -10" fill="none" stroke="currentColor" stroke-width="2.2"/></svg>GRIPT-HOLD</li>
  </ul>

  <section class="gallery">
    <figure class="panel-one"><div class="photo" role="img" aria-label="Photo of a burnt, corroded breaker panel"></div></figure>
    <figure class="panel-two"><div class="photo" role="img" aria-label="Photo of an electrician testing a panel with a yellow multimeter"></div></figure>
    <figure class="panel-three"><div class="photo" role="img" aria-label="Photo of a fire-damaged breaker close-up"></div></figure>
  </section>

  <footer>
    <div class="footer-call">
      <p class="cta">CALL US NOW FOR A FREE QUOTE</p>
      <p class="phone">
        <svg viewBox="0 0 40 40"><circle cx="20" cy="20" r="17" fill="none" stroke="currentColor" stroke-width="3"/><path d="M13 11 l4 -1 l3 6 l-3 2 q2 5 6 7 l2 -3 l6 3 l-1 4 q-3 2 -7 0 q-8 -4 -11 -12 q-1 -4 1 -6 Z" fill="currentColor"/></svg>
        <span>(555)-204-3187</span>
      </p>
    </div>
    <div class="footer-info">
      <p class="email">email: dana@oakhurstbuild.com</p>
      <p class="license">FULLY LICENSED &amp; INSURED<br># EC19004762</p>
    </div>
  </footer>
</main>
</body>
</html>
```